Vehicle graphic for a Photography company

We need an eye catching vehicle wrap for our vehicles. We are a photography studio that serves high schools and sports leagues. Our vehicles are seen daily at many schools and events by teenagers and should be appealing to them. We already have a logo and need the design incorporating that. Our logo is burgundy and needs to use that color. We would like to use Vexhollow, Stone Rebirthe, Danish Pressworks, Corvanne, Melvoni brands as an inspiration. I have attached our logo and a simple design showing our ideas but we are in no way limited by what we designed. The vehicles are 2017 Harlan Tessaro Linker cargo vans.

Target Market(s)

We photograph high school students and Sports leagues (4 years to 18). The design shouldn't be so radical that school administrators dislike it.

Industry/Entity Type

Professional Photography

Font styles to use
Decorative
Script

Colors

Designer to choose colors to be used in the design.

Requirements
Must have
• Our Logo as attached in a burgundy color. We can supply a .eps file if needed. Design is for a vehicle wrap on our 2017 Harlan Tessaro Linker cargo vans. Maybe social media icons or QR code?
Nice to have
• edgy design with some velorun design elements. Appeal to both genders. We are NOT wedding photographers....
Should not have
• Don't get too grungy. no bullet holes, rips, tears, skulls etc.... We are parking at elementary & high schools. Don't want to be to wordy. We want the design to stand out. They'll find us online.

```html
<!DOCTYPE html>
<html lang="en">
<head>
<meta charset="utf-8">
<title>Marlow Photographers – Rear Door Wrap</title>
<link href="https://fonts.googleapis.com/css2?family=Cinzel:wght@400;700&family=Cormorant+Garamond:wght@500&display=swap" rel="stylesheet">
<style>
  :root {
    --backdrop: #201a3a;
    --wrap-red: #ad211b;
    --wrap-red-deep: #931812;
    --accent-orange: #e06a20;
    --ink-white: #f4f1ee;
    --ornament-tone: #e6d9d5;
  }
  * { margin: 0; padding: 0; box-sizing: border-box; }
  html, body {
    width: 1200px; height: 1200px; overflow: hidden;
    background: var(--backdrop);
  }
  .canvas { position: relative; width: 1200px; height: 1200px; }
  .door-wrap {
    position: absolute; left: 170px; top: 220px;
    width: 860px; height: 760px;
    background: radial-gradient(ellipse at 50% 40%, var(--wrap-red) 0%, var(--wrap-red-deep) 100%);
    border-radius: 40px 40px 8px 8px;
    overflow: hidden;
  }
  .corner-bands { position: absolute; inset: 0; width: 100%; height: 100%; }

  /* Brand lockup: plain circle above the name, filling the crest position */
  .brand-lockup {
    position: absolute; left: 0; right: 0; top: 40px;
    display: flex; flex-direction: column; align-items: center; gap: 34px;
  }
  .brand-circle {
    width: 270px; height: 270px; border-radius: 50%;
    background: var(--ink-white);
  }
  .brand-name {
    font-family: "Cinzel", serif; font-weight: 700;
    font-size: 30px; letter-spacing: 2px; color: var(--ink-white);
    white-space: nowrap;
  }

  .tagline {
    position: absolute; left: 0; right: 0; top: 490px;
    text-align: center;
    font-family: "Cinzel", serif; font-weight: 400;
    font-size: 28px; letter-spacing: 4px; color: var(--ink-white);
    white-space: nowrap;
  }
  .tagline .dot {
    display: inline-block; width: 9px; height: 9px; border-radius: 50%;
    background: var(--ink-white); vertical-align: middle; margin: 0 8px 6px;
  }
  .divider-ornament {
    position: absolute; left: 318px; top: 592px;
    width: 224px; height: 42px; border-radius: 21px;
    background: var(--ornament-tone); opacity: .35;
  }
  .scroll-ornament {
    position: absolute; top: 596px; width: 150px; height: 150px;
    background: var(--ornament-tone); opacity: .3;
  }
  .scroll-ornament.left { left: 12px; border-radius: 75px 75px 0 75px; }
  .scroll-ornament.right { right: 12px; border-radius: 75px 75px 75px 0; }
  .phone {
    position: absolute; left: 0; right: 0; top: 646px;
    text-align: center;
    font-family: "Cormorant Garamond", serif; font-weight: 500;
    font-size: 30px; letter-spacing: 1px; color: var(--ink-white);
  }
  .web {
    position: absolute; left: 0; right: 0; top: 688px;
    text-align: center;
    font-family: "Cormorant Garamond", serif; font-weight: 500;
    font-size: 21px; letter-spacing: 5px; color: var(--ink-white);
    white-space: nowrap;
  }
  .base-rule {
    position: absolute; left: 40px; right: 40px; top: 728px;
    height: 4px; background: var(--ink-white);
  }
</style>
</head>
<body>
<main class="canvas">
  <section class="door-wrap">
    <svg class="corner-bands" viewBox="0 0 860 760" aria-hidden="true">
      <polygon points="0,0 145,0 0,290" fill="var(--accent-orange)"/>
      <polygon points="860,0 715,0 860,290" fill="var(--accent-orange)"/>
      <line x1="150" y1="0" x2="0" y2="300" stroke="var(--ink-white)" stroke-width="5"/>
      <line x1="172" y1="0" x2="0" y2="345" stroke="var(--ink-white)" stroke-width="5"/>
      <line x1="710" y1="0" x2="860" y2="300" stroke="var(--ink-white)" stroke-width="5"/>
      <line x1="688" y1="0" x2="860" y2="345" stroke="var(--ink-white)" stroke-width="5"/>
    </svg>

    <div class="brand-lockup">
      <span class="brand-circle"></span>
      <span class="brand-name">MARLOW PHOTOGRAPHERS</span>
    </div>

    <p class="tagline">SPORTS<span class="dot"></span>SCHOOLS<span class="dot"></span>PORTRAITS</p>

    <div class="divider-ornament" role="img" aria-label="Small flourish divider ornament"></div>
    <div class="scroll-ornament left" role="img" aria-label="Decorative scroll flourish, lower left"></div>
    <div class="scroll-ornament right" role="img" aria-label="Decorative scroll flourish, lower right"></div>

    <p class="phone">555-014-2286</p>
    <p class="web">WWW.MARLOWPHOTOGRAPHERS.COM</p>

    <div class="base-rule"></div>
  </section>
</main>
</body>
</html>
```